Small Unique Manufacturer Needs a facelift for eCommerce Wordpress Site

We need a wordpress template design that brands our business based in Minneapolis, MN called "Lantern Socials". Lantern Socials manufacturers and assembles fraternity and sorority paddle kits for Sisterhood parties and fraternity rush and pledge process decoration parties. We're our site is an eCommerce site that runs at LanternSocials.example. We'd like an attractive design that's more on the feminine side (rather than masculine) as our primary consumer will be female. However as we move into the future we will have products for the fraternities as well.
We like earthy neutral colors, our products are unfinished pine, walnut, and oak, but we're not keen on focusing on woodgrain designs, etc.
The final design should communicate fun, be clean, clear, and bright, and appeal to the millennial generation and must be fully functional.
We're currently using the CartWillow plugin for our eCommerce back end and like it.

Target Market(s)

College greeks. Fraternity and Sorority Members

Industry/Entity Type

Business

Font styles to use
Sans Serif

Colors
cde8f3
ecf7fa
f9d9e8
fbc994

Requirements
Must have
• Clean, clear design. A nice branding project start to finish. Millennial focus.
• Must work with our current CartWillow page.
Should not have
• Anything that looks down or talks down to college students.

```html
<!DOCTYPE html>
<html lang="en">
<head>
<meta charset="utf-8">
<title>Lantern Socials</title>
<link rel="stylesheet" href="https://fonts.googleapis.com/css2?family=Arimo:wght@400;700&display=swap">
<style>
:root{
  --sky:#cde8f3;
  --mist:#ecf7fa;
  --blush:#f9d9e8;
  --peach:#fbc994;
  --peach-soft:#fcd3a6;
  --peach-deep:#e9a66a;
  --price:#d98c4c;
  --plum:#8c4a5c;
  --rose:#a24f63;
  --ink:#333;
  --body:#555;
  --muted:#888;
  --footer:#dcebf4;
  --green:#6cae1a;
}
*{box-sizing:border-box;margin:0;padding:0}
html,body{width:1038px;height:1200px;overflow:hidden;background:#fff}
body{position:relative;font-family:"Arimo",Arial,sans-serif;color:var(--body)}
.abs{position:absolute}
.topline{left:0;top:0;width:1038px;height:5px;background:var(--sky)}
.account{top:10px;left:632px;font-size:6.5px;color:var(--muted);white-space:nowrap}
.cart{left:691px;top:5px;width:75px;height:20px;background:var(--sky);font-size:6.5px;color:var(--muted);display:flex;align-items:center;gap:13px;padding-left:7px}
.logo{left:259px;top:38px;font-size:25px;color:var(--plum);font-weight:400;white-space:nowrap}
.nav-item{top:49px;font-size:6.5px;color:#555;white-space:nowrap}
.hero{left:0;top:86px;width:1038px;height:244px;background:var(--peach)}
.hero-shadow{left:370px;top:80px;width:300px;height:12px;border-radius:50%;box-shadow:0 6px 8px rgba(0,0,0,.18)}
.hero-title{left:260px;top:152px;font-size:20px;font-weight:400;color:var(--ink);white-space:nowrap}
.hero-copy{left:260px;top:182px;width:250px;font-size:7.5px;line-height:10px;color:#555}
.price-box{left:260px;top:217px;width:214px;height:51px;background:var(--peach-soft)}
.buy-btn{left:270px;top:229px;width:86px;height:29px;background:var(--peach-deep);color:#fbe6cf;font-size:7px;display:flex;align-items:center;justify-content:center;text-transform:uppercase}
.hero-price{left:364px;top:229px;font-size:25px;color:var(--price)}
.fill{display:block}
.promo-title{top:364px;font-size:8.5px;font-weight:700;color:var(--rose)}
.promo-tag{width:96px;height:33px;background:var(--peach);color:#fff;text-align:center;padding-top:3px}
.promo-tag b{display:block;font-size:15px;font-weight:400}
.promo-tag i{display:block;font-size:6.5px;font-style:normal;font-weight:700}
.promo-copy{top:499px;width:225px;font-size:7px;line-height:9.5px}
.section-title{font-size:7.5px;font-weight:700;color:var(--rose);text-transform:uppercase}
.featured{left:259px;top:568px;width:507px;height:150px;background:var(--blush)}
.featured-title{left:276px;top:583px;font-size:11px;font-weight:400;color:#555;text-transform:uppercase;white-space:nowrap}
.featured-copy{left:276px;top:608px;width:150px;font-size:6.6px;line-height:9.6px}
.view-all{left:276px;top:655px;font-size:5.5px;font-weight:700;color:#555;text-transform:uppercase}
.fcard{top:584px;width:96px;height:112px;background:#fff}
.fcard .price{position:absolute;left:0;bottom:0;width:96px;height:22px;background:var(--mist);font-size:7px;font-weight:700;color:#777;display:flex;align-items:center;justify-content:center;gap:4px}
.fcard s{font-weight:400;color:#999}
.recent-title{top:882px;font-size:11px;font-weight:400;color:var(--rose);text-transform:uppercase;white-space:nowrap}
.rcopy{top:900px;width:117px;font-size:6.8px;line-height:9px}
.rbar{top:940px;width:117px;height:24px;background:var(--sky);display:flex;align-items:center;justify-content:space-between;padding:0 8px;font-size:6.5px;color:#777;text-transform:uppercase}
.rbar b{color:var(--rose)}
.footer{left:0;top:1006px;width:1038px;height:194px;background:var(--footer)}
.fhead{font-size:10px;color:#555;white-space:nowrap}
.frule{height:1px;background:#c7dbe6}
.flinks{font-size:6.5px;line-height:9.2px;color:#666;white-space:nowrap}
.email{left:645px;top:1062px;width:78px;height:19px;background:#fff;font-size:6.5px;color:#aaa;padding:6px 4px}
.signup{left:723px;top:1062px;width:43px;height:19px;background:var(--green);color:#fff;font-size:6.5px;font-weight:700;display:flex;align-items:center;justify-content:center}
.social{top:1127px;width:14px;height:14px;border-radius:2px}
.copyright{left:259px;top:1176px;font-size:6.5px;color:#666}
.pay{top:1170px;width:28px;height:18px;background:#fff;border:1px solid #ccd;font-size:5.5px;font-weight:700;color:#557;display:flex;align-items:center;justify-content:center}
</style>
</head>
<body>
<div class="abs topline"></div>
<div class="abs account">Login &nbsp;|&nbsp; Register</div>
<div class="abs cart">
  <svg width="13" height="10" viewBox="0 0 13 10"><path d="M0 1h2l2 6h7l1.5-5H3" fill="none" stroke="#6b8a98" stroke-width="1.3"/><circle cx="5" cy="9" r="1" fill="#6b8a98"/><circle cx="10" cy="9" r="1" fill="#6b8a98"/></svg>
  <span>CART ( 0 )</span>
</div>
<div class="abs logo">Lantern Socials</div>
<nav>
  <span class="abs nav-item" style="left:556px">HOME</span>
  <span class="abs nav-item" style="left:598px">SHOP</span>
  <span class="abs nav-item" style="left:636px">CUSTOM LINK</span>
  <span class="abs nav-item" style="left:701px">BLOG</span>
  <span class="abs nav-item" style="left:737px">CONTACT</span>
</nav>

<section>
  <div class="abs hero"></div>
  <div class="abs hero-shadow"></div>
  <h1 class="abs hero-title">Clean &amp; Powerful!</h1>
  <p class="abs hero-copy">Lorem Ipsum is simply dummy text of the printing and typesetting industry. Lorem Ipsum has been the industry's standard dummy text</p>
  <div class="abs price-box"></div>
  <div class="abs buy-btn">Purchase now!</div>
  <div class="abs hero-price">$1234.00</div>
  <div class="abs fill" role="img" aria-label="Large engraved wooden paddle with letters and crest" style="left:614px;top:110px;width:54px;height:206px;background:linear-gradient(90deg,#c9963e,#e5bd6c,#c9963e);border-radius:6px"></div>
  <div class="abs fill" role="img" aria-label="Smaller engraved wooden paddle with letters" style="left:680px;top:120px;width:29px;height:170px;background:linear-gradient(90deg,#c9963e,#e5bd6c,#c9963e);border-radius:5px"></div>
</section>

<section>
  <div class="abs promo-title" style="left:259px">Lorem Ipsum is simply dummy text</div>
  <div class="abs fill" role="img" aria-label="Row of dark and light wooden paddles" style="left:259px;top:384px;width:237px;height:104px;background:linear-gradient(90deg,#f2f2f2,#c56a3a 35%,#a8562c 60%,#5a3422 85%,#eee)"></div>
  <div class="abs promo-tag" style="left:270px;top:446px"><b>$12.00</b><i>SHOP NOW!</i></div>
  <p class="abs promo-copy" style="left:259px">Lorem ipsum dolor sit amet, consectetur adip iscing elit. Sed velit dui, placerat a fermentum in, ullam corper id elit.</p>

  <div class="abs promo-title" style="left:528px">Lorem Ipsum is simply dummy text</div>
  <div class="abs fill" role="img" aria-label="Close view of a wooden paddle blade on grass" style="left:528px;top:384px;width:238px;height:104px;background:linear-gradient(160deg,#6c7a3e,#5a3a4a 25%,#c88a48 45%,#d9a763 75%,#b97a3a)"></div>
  <div class="abs promo-tag" style="left:540px;top:446px"><b>$12.00</b><i>SHOP NOW!</i></div>
  <p class="abs promo-copy" style="left:528px">Lorem ipsum dolor sit amet, consectetur adip iscing elit. Sed velit dui, placerat a fermentum in, ullam corper id elit.</p>
</section>

<section>
  <div class="abs section-title" style="left:259px;top:551px">Featured Products</div>
  <div class="abs featured"></div>
  <h2 class="abs featured-title">Lorem Ipsum is simply</h2>
  <p class="abs featured-copy">Lorem Ipsum is simply dummy text of the printing and typesetting industry. Lorem Ipsum has been the industry's standard dummy text ever since the 1500s, when an unknown</p>
  <div class="abs view-all">View all products</div>

  <div class="abs fcard" style="left:442px">
    <div class="abs fill" role="img" aria-label="Engraved wooden paddle with letters" style="left:28px;top:0;width:40px;height:90px;background:linear-gradient(90deg,#c08a3c,#e0b56a,#c08a3c)"></div>
    <div class="price">$123.00</div>
  </div>
  <div class="abs fcard" style="left:548px">
    <div class="abs fill" role="img" aria-label="Three blank paddles in walnut, oak and pine" style="left:4px;top:4px;width:88px;height:80px;background:linear-gradient(90deg,#6b4424,#6b4424 30%,#d2a062 35%,#d2a062 63%,#efdcb2 68%)"></div>
    <div class="price">$123.00</div>
  </div>
  <div class="abs fcard" style="left:654px">
    <div class="abs fill" role="img" aria-label="Group of decorated paddles with crests" style="left:4px;top:2px;width:88px;height:84px;background:linear-gradient(90deg,#d3a565,#e7c68e,#c9954f)"></div>
    <div class="price"><s>$123.00</s> $123.00</div>
  </div>
</section>

<section>
  <div class="abs section-title" style="left:259px;top:749px">Recent Products</div>

  <div class="abs fill" role="img" aria-label="Fan of wooden paddles in mixed tones" style="left:259px;top:768px;width:117px;height:100px;background:linear-gradient(90deg,#d08a4a,#7a3e1e,#e0b272,#5a2c18,#d6a060)"></div>
  <h3 class="abs recent-title" style="left:259px">Lorem Ipsum</h3>
  <p class="abs rcopy" style="left:259px">Lorem ipsum dolor sit amet, consectetur adipiscing elit. Nullam vulputate, metus tempus malesuada lacinia, lorem sapien</p>
  <div class="abs rbar" style="left:259px"><span>Add to cart</span><b>$123.00</b></div>

  <div class="abs fill" role="img" aria-label="Dark paddle with a red stripe" style="left:390px;top:768px;width:116px;height:100px;background:linear-gradient(90deg,#2a2a2a 40%,#b4532e 48%,#8a3a22 54%,#2a2a2a 62%)"></div>
  <h3 class="abs recent-title" style="left:390px">Lorem Ipsum</h3>
  <p class="abs rcopy" style="left:390px">Lorem ipsum dolor sit amet, consectetur adipiscing elit. Nullam vulputate, metus tempus malesuada lacinia</p>
  <div class="abs rbar" style="left:390px"><span>Add to cart</span><b>$123.00</b></div>

  <div class="abs fill" role="img" aria-label="Decorated paddles with letters and crests" style="left:520px;top:768px;width:116px;height:100px;background:linear-gradient(90deg,#f2f2f2,#d7aa6a 25%,#e6c48c 55%,#cf9d5a 80%,#eee)"></div>
  <h3 class="abs recent-title" style="left:520px">Lorem Ipsum</h3>
  <p class="abs rcopy" style="left:520px">Lorem ipsum dolor sit amet, consectetur adipiscing elit. Nullam vulputate, metus tempus malesuada</p>
  <div class="abs rbar" style="left:520px"><span>Add to cart</span><b>$123.00</b></div>

  <div class="abs fill" role="img" aria-label="Slim wooden paddles leaning together" style="left:649px;top:768px;width:117px;height:100px;background:linear-gradient(90deg,#f0f0f0,#c9683a 30%,#e6e6e6 45%,#5a3a2a 60%,#eee 75%)"></div>
  <h3 class="abs recent-title" style="left:649px">Lorem Ipsum</h3>
  <p class="abs rcopy" style="left:649px">Lorem ipsum dolor sit amet, consectetur adipiscing elit. Nullam vulputate, metus tempus</p>
  <div class="abs rbar" style="left:649px"><span>Add to cart</span><b>$123.00</b></div>
</section>

<footer>
  <div class="abs footer"></div>
  <div class="abs fhead" style="left:259px;top:1034px">Site Info</div>
  <div class="abs frule" style="left:259px;top:1050px;width:160px"></div>
  <div class="abs flinks" style="left:259px;top:1058px">Shipping and Return<br>Right of Withdraw<br>Imprint<br>Privacy Notice<br>Contact Us</div>
  <div class="abs flinks" style="left:382px;top:1058px">Create New Account<br>Login<br>Track your order<br>Shopping Cart</div>

  <div class="abs fhead" style="left:498px;top:1034px">Latest Blog Post</div>
  <div class="abs frule" style="left:498px;top:1050px;width:96px"></div>
  <div class="abs flinks" style="left:498px;top:1067px">Lorem Ipsum is simply dummy text</div>
  <div class="abs frule" style="left:498px;top:1081px;width:96px"></div>
  <div class="abs flinks" style="left:498px;top:1085px">Lorem Ipsum is simply dummy text</div>
  <div class="abs frule" style="left:498px;top:1099px;width:96px"></div>
  <div class="abs flinks" style="left:498px;top:1101px">Lorem Ipsum is simply dummy text</div>

  <div class="abs fhead" style="left:645px;top:1033px">Newsletter</div>
  <div class="abs email">email@example.com</div>
  <div class="abs signup">SIGN UP</div>
  <div class="abs fhead" style="left:645px;top:1103px;font-size:9px">Social Link</div>
  <div class="abs frule" style="left:645px;top:1118px;width:121px"></div>
  <div class="abs social" style="left:645px;background:#6d86a8" aria-label="Social link"></div>
  <div class="abs social" style="left:665px;background:#7cb3d0" aria-label="Social link"></div>
  <div class="abs social" style="left:685px;background:#8a8a8a" aria-label="Social link"></div>
  <div class="abs social" style="left:705px;background:#e0a070" aria-label="Social link"></div>

  <div class="abs frule" style="left:259px;top:1162px;width:507px"></div>
  <div class="abs copyright">Copyright © 2014 Company Name</div>
  <div class="abs pay" style="left:674px">Payvio</div>
  <div class="abs pay" style="left:705px">Cardix</div>
  <div class="abs pay" style="left:737px">Vantra</div>
</footer>
</body>
</html>
```